KLT Business cards

I currently have a logo that was designed by a sketch harbor designer. I would like this to be added to the business card.

We are an innovative new start-up business offering finance solutions to the car dealership market in the UK. So our clients are quiet traditional, so are cards need to fit in, but at the same time show we are a modern online business.

Industry/Entity Type

Finance

```html
<!DOCTYPE html>
<html lang="en">
<head>
<meta charset="utf-8">
<title>KLT Business Cards</title>
<link rel="stylesheet" href="https://fonts.googleapis.com/css2?family=Open+Sans:wght@400;600;700&display=swap">
<style>
  :root {
    --backdrop: #959595;
    --navy: #10284b;
    --paper: #e5e5e5;
    --ink: #2f3133;
    --white: #f2f2f2;
    --faint: #d2d2d2;
  }
  * { margin: 0; padding: 0; box-sizing: border-box; }
  html, body { width: 1200px; height: 1000px; overflow: hidden; }
  body {
    position: relative;
    background: var(--backdrop);
    font-family: "Open Sans", Arial, sans-serif;
  }
  .card {
    position: absolute;
    left: 260px;
    width: 680px;
    height: 386px;
    overflow: hidden;
  }
  .card--front { top: 82px; background: var(--navy); }
  .card--back { top: 537px; background: var(--paper); }

  .brand { position: absolute; display: flex; align-items: center; }
  .brand__mark { flex: none; }
  .brand__name {
    font-weight: 400;
    line-height: 1.18;
  }
  .card--front .brand { left: 180px; top: 128px; }
  .card--front .brand__mark { margin-right: 20px; }
  .card--front .brand__name { color: var(--white); font-size: 37px; }

  .card--back .brand { left: 25px; top: 128px; }
  .card--back .brand__mark { margin-right: 20px; }
  .card--back .brand__name { color: var(--navy); font-size: 34px; }

  .divider {
    position: absolute;
    left: 340px; top: 85px;
    width: 2px; height: 213px;
    background: var(--ink);
  }
  .backdrop-ring {
    position: absolute;
    left: 370px; top: 132px;
  }
  .contact {
    position: absolute;
    left: 371px; top: 104px;
    color: var(--ink);
  }
  .contact__name { font-size: 25px; font-weight: 700; line-height: 1.1; }
  .contact__role {
    font-size: 15px; font-weight: 600; color: var(--navy);
    letter-spacing: 0.5px; margin-bottom: 22px;
  }
  .contact__list { list-style: none; font-size: 14.5px; line-height: 28.5px; }
  .tagline {
    position: absolute;
    left: 0; right: 0; top: 348px;
    text-align: center;
    font-size: 16px;
    letter-spacing: 5.5px;
    color: var(--ink);
  }
  .band {
    position: absolute;
    left: 0; right: 0; bottom: 0;
    height: 10px;
    background: var(--navy);
  }
</style>
</head>
<body>
  <section class="card card--front" aria-label="Card front">
    <div class="brand">
      <svg class="brand__mark" width="134" height="134" viewBox="0 0 134 134" aria-hidden="true">
        <circle cx="67" cy="67" r="62" fill="none" stroke="var(--white)" stroke-width="5"/>
      </svg>
      <div class="brand__name">Kerb<br>Line<br>Trust</div>
    </div>
  </section>

  <section class="card card--back" aria-label="Card back">
    <svg class="backdrop-ring" width="320" height="320" viewBox="0 0 320 320" aria-hidden="true">
      <circle cx="160" cy="160" r="150" fill="none" stroke="var(--faint)" stroke-width="12"/>
    </svg>
    <div class="brand">
      <svg class="brand__mark" width="124" height="124" viewBox="0 0 124 124" aria-hidden="true">
        <circle cx="62" cy="62" r="57" fill="none" stroke="var(--navy)" stroke-width="5"/>
      </svg>
      <div class="brand__name">Kerb<br>Line<br>Trust</div>
    </div>
    <div class="divider"></div>
    <div class="contact">
      <p class="contact__name">Daniel Marsh</p>
      <p class="contact__role">FOUNDER</p>
      <ul class="contact__list">
        <li>Mobile: 07700 900418</li>
        <li>daniel.marsh@kerblinetrust.com</li>
        <li>Chat: daniel.marsh_klt</li>
        <li>www.kerblinetrust.com</li>
      </ul>
    </div>
    <p class="tagline">DRIVE NOW, PAY LATER.</p>
    <div class="band"></div>
  </section>
</body>
</html>
```